Business card for a plastic surgeon

i need a business card for a plastic surgeon. I have two adresses. The card should communicate safety, simmetry, beauty and with soft colors.
What i want in the card:
- my logo: Letters "R"and "B" (picture uploaded)
- my name: Renato Bastiani
- my registration: CRM 507 219
- my adresses and phone numbers (2):
- Av Dr Teixeira Lopes, 2710, sala 305 - Vila Olímpia | São Paulo/ SP - Phone: 11 4172-5036
- Al. Itapeva, 47, 3 andar - Alphaville | Barueri/ SP - Phone: 11 6350-2481

- my social network: site, facebook and instagram

Target Market(s)

people (95% girls and women) that want cosmetic procedures and plastic surgery

Industry/Entity Type

Business

Contact Information for Business Card

The card should communicate safety, simmetry, beauty and with soft colors.
Beige, brown, gray, rosy are some options. Color is free

Font styles to use
Serif

Requirements
Must have
• - my logo: Letters "R"and "B" (picture uploaded)
• - my name: Renato Bastiani
• - my registration: CRM 507 219
• - my adresses and phone numbers (2):
• - Av Dr Teixeira Lopes, 2710, sala 305 - Vila Olímpia | São Paulo/ SP - Phone: 11 4172-5036
• - Al. Itapeva, 47, 3 andar - Alphaville | Barueri/ SP - Phone: 11 6350-2481
• - my social network: site, facebook and instagram
Should not have
• other images (only my logo)

```html
<!DOCTYPE html>
<html lang="pt-BR">
<head>
<meta charset="utf-8">
<title>Renato Bastiani – Business Card</title>
<link rel="stylesheet" href="https://fonts.googleapis.com/css2?family=Cinzel:wght@400;500&family=Tinos:wght@400&display=swap">
<style>
  :root {
    --stage: #2a2a2a;
    --rose: #bd8f8f;
    --paper: #ffffff;
    --ink: #3a3a3a;
    --ink-soft: #555555;
    --accent: #c08080;
    --on-rose: #ffffff;
  }
  * { box-sizing: border-box; margin: 0; padding: 0; }
  html, body { width: 1200px; height: 852px; overflow: hidden; }
  body {
    background: var(--stage);
    display: flex;
    align-items: center;
    justify-content: center;
    gap: 40px;
  }
  .card {
    position: relative;
    width: 540px;
    height: 309px;
    box-shadow: 0 10px 30px rgba(0,0,0,.45);
  }

  /* Front side */
  .card--front {
    background: var(--rose);
    color: var(--on-rose);
    font-family: "Cinzel", serif;
    display: flex;
    flex-direction: column;
    align-items: center;
    justify-content: center;
    gap: 22px;
  }
  .monogram {
    display: flex;
    align-items: center;
    gap: 8px;
    font-family: "Cinzel", serif;
    font-size: 18px;
    letter-spacing: 2px;
  }
  .monogram__dot {
    width: 10px; height: 10px;
    border-radius: 50%;
    background: currentColor;
  }
  .monogram--light { color: var(--on-rose); }
  .monogram--dark { color: var(--ink-soft); }
  .front__name {
    font-size: 25px;
    font-weight: 400;
    letter-spacing: 1px;
    text-align: center;
    line-height: 1.1;
  }
  .front__title {
    font-size: 13px;
    letter-spacing: 4.5px;
    text-align: center;
    margin-top: 4px;
  }

  /* Back side */
  .card--back {
    background: var(--paper);
    color: var(--ink);
    font-family: "Tinos", serif;
  }
  .card--back .monogram {
    position: absolute;
    top: 48px;
    right: 52px;
  }
  .social {
    position: absolute;
    right: 30px;
    top: 148px;
    display: flex;
    align-items: center;
    gap: 6px;
    font-size: 12px;
    color: var(--ink-soft);
  }
  .social__mark {
    width: 12px; height: 12px;
    background: var(--ink-soft);
  }
  .back__identity {
    position: absolute;
    left: 34px;
    top: 168px;
  }
  .back__name {
    font-size: 18px;
    letter-spacing: .5px;
    font-weight: 400;
  }
  .back__registration {
    font-size: 11px;
    color: var(--accent);
    margin-top: 1px;
  }
  .back__addresses {
    position: absolute;
    left: 34px;
    bottom: 30px;
    font-size: 10.5px;
    line-height: 1.35;
    font-style: normal;
  }
  .address + .address { margin-top: 6px; }
</style>
</head>
<body>
  <section class="card card--front" aria-label="Front of business card">
    <div class="monogram monogram--light"><span class="monogram__dot"></span>Bastiani</div>
    <div>
      <h1 class="front__name">DR. RENATO BASTIANI</h1>
      <p class="front__title">CIRURGIÃO PLÁSTICO</p>
    </div>
  </section>

  <section class="card card--back" aria-label="Back of business card">
    <div class="monogram monogram--dark"><span class="monogram__dot"></span>Bastiani</div>
    <div class="social"><span class="social__mark"></span>@rbastiani</div>
    <div class="back__identity">
      <h2 class="back__name">RENATO BASTIANI</h2>
      <p class="back__registration">Registration N: CRM 507 219</p>
    </div>
    <address class="back__addresses">
      <p class="address">Av Dr Teixeira Lopes, 2710, sala 305<br>Vila Olímpia | São Paulo/ SP<br>P: 11 4172-5036</p>
      <p class="address">Al. Itapeva, 47, 3 andar - Alphaville | Barueri/ SP<br>P: 11 6350-2481</p>
    </address>
  </section>
</body>
</html>
```